Corporate Design für Helga Brunnmeier
Zielgruppe
Ich bin eine Beraterin mit sehr unterschiedlichen Zugängen. Zum einen mache ich hellsichtige Beratungen, zum anderen Organisationsberatungen und Coaching. Ich habe für jedes Problem eine Lösung. Es handelt sich um eine außergewöhnliche Dienstleistung. Es geht um mehr Klarheit und Transparenz. Meine Kunden sind sowohl Privatpersonen, als auch Firmeninhaber und Firmenchefs kleiner und großer Unternehmen.
I am a consultant with different approaches. On one hand I am doing perceptive consulting, on the other hand I do systemic consulting of organizations and coaching. I find a solution for every problem. It is an outstanding service. Clearness and transparency are mainly wished. My clients are private persons as well as company owners and managers of small and huge companies.
Aufgabenstellung
Das Logo soll nur den Vor- und Nachnamen beinhalten und elegant, weiblich, warm, herzlich sein sowie Lebensfreude, Erleichterung und Exklusivität suggerieren.
Das Logo soll auf den Visitenkarten auf der Rückseite geprägt werden. Es soll aber auch für Briefpapier, Powerpoint-Vorlage und Website gut tauglich sein.
The logo should include only my full name. It should be elegant, female, warm, sincere as well as suggest joie de vivre, easement and exclusiveness.
The logo should be stamped on the back side of the business cards. It should also work for letters, PowerPoint presentations and on the website.

```html
<!DOCTYPE html>
<html lang="de">
<head>
<meta charset="utf-8">
<title>Helga Brunnmeier – Geschäftsausstattung</title>
<link rel="stylesheet" href="https://fonts.googleapis.com/css2?family=Mukta:wght@300;400&display=swap">
<style>
  :root {
    --gold: #c59a14;
    --gold-faint: #f6e6c4;
    --paper: #fffdf6;
    --ink: #1e1e1e;
    --edge: #222;
    --shadow: rgba(0,0,0,0.28);
    --bg: #ffffff;
  }
  * { box-sizing: border-box; margin: 0; padding: 0; }
  html, body { width: 1200px; height: 848px; overflow: hidden; background: var(--bg); }
  body { position: relative; font-family: "Mukta", sans-serif; font-weight: 300; color: var(--ink); }

  .wordmark {
    position: absolute; color: var(--gold); font-family: "Mukta", sans-serif;
    font-weight: 400; letter-spacing: 0.04em; text-transform: uppercase; white-space: nowrap; line-height: 1;
  }
  .wordmark--hero { left: 52px; top: 56px; font-size: 44px; }

  .sheet {
    position: absolute; background: var(--paper); border: 1px solid var(--edge);
    box-shadow: 6px 6px 6px var(--shadow);
  }
  .card { width: 188px; height: 121px; left: 53px; }
  .card--front { top: 354px; }
  .card--back { top: 520px; }
  .letter { width: 397px; height: 561px; top: 230px; }
  .letter--first { left: 322px; }
  .letter--follow { left: 744px; }

  .label { color: var(--gold); }
  .block { position: absolute; line-height: 1.45; white-space: nowrap; }

  .card--front .wordmark { left: 14px; top: 16px; font-size: 16px; }
  .card__name { left: 14px; top: 73px; font-size: 7px; color: var(--gold); }
  .card__address { left: 14px; top: 92px; font-size: 6.5px; }
  .card__rule { position: absolute; left: 77px; top: 75px; width: 1px; height: 34px; background: var(--gold); }
  .card__contact { left: 90px; top: 73px; font-size: 6.2px; }

  .card--back .wordmark { left: 50%; top: 50%; transform: translate(-50%, -50%); font-size: 15px; color: var(--gold-faint); }

  .letter--first .wordmark { left: 50%; top: 26px; transform: translateX(-50%); font-size: 16px; }
  .letter__sender { left: 37px; top: 82px; font-size: 5px; }
  .letter__info { left: 297px; top: 113px; font-size: 5.6px; }
  .letter__info p + p { margin-top: 5px; }
  .letter__fold { position: absolute; left: 10px; top: 196px; width: 3px; height: 3px; border-radius: 50%; background: var(--gold); }
  .letter__bank { left: 297px; top: 493px; font-size: 5.2px; }
</style>
</head>
<body>

  <div class="wordmark wordmark--hero">Helga Brunnmeier</div>

  <section class="sheet card card--front" aria-label="Visitenkarte Vorderseite">
    <div class="wordmark">Helga Brunnmeier</div>
    <div class="block card__name">Helga Brunnmeier</div>
    <div class="block card__address">Lindenweg 12<br>A 8045 Talheim</div>
    <span class="card__rule"></span>
    <div class="block card__contact">
      <span class="label">Fon</span> +43 (0) 3150-27384<br>
      <span class="label">Mobil</span> +43 (0) 660-31 4477 29<br>
      <span class="label">mail</span> office@helgabrunnmeier.com<br>
      <span class="label">web</span> www.helgabrunnmeier.com
    </div>
  </section>

  <section class="sheet card card--back" aria-label="Visitenkarte Rückseite">
    <div class="wordmark">Helga Brunnmeier</div>
  </section>

  <section class="sheet letter letter--first" aria-label="Briefbogen erste Seite">
    <div class="wordmark">Helga Brunnmeier</div>
    <div class="block letter__sender">Helga Brunnmeier · Lindenweg 12 · A 8045 Talheim</div>
    <div class="block letter__info">
      <p class="label">Helga Brunnmeier</p>
      <p>Lindenweg 12<br>A 8045 Talheim</p>
      <p>
        <span class="label">Fon</span> +43 (0) 3150-27384<br>
        <span class="label">Mobil</span> +43 (0) 660-31 4477 29<br>
        <span class="label">mail</span> office@helgabrunnmeier.com<br>
        <span class="label">web</span> www.helgabrunnmeier.com
      </p>
    </div>
    <span class="letter__fold"></span>
    <div class="block letter__bank">
      <span class="label">Konto</span> Musterbank<br>
      <span class="label">IBAN</span> AT 12 3456 7899 1111 0000 00<br>
      <span class="label">BIC</span> MUSTER000XXX<br>
      <span class="label">Gerichtsstand</span> MUSTERSTADT...
    </div>
  </section>

  <section class="sheet letter letter--follow" aria-label="Briefbogen Folgeseite"></section>

</body>
</html>
```